Property Services Company Needs a Brochure Design

Looking for a new brochure design for an existing property services company.

We provide a range of property services from, market research, real estate brokerage, valuation and appraisal, property development and other real estate consulting services.

We would like a fresh modern brochure design with good graphics and features. Our colours are white, blue and orange.

The design should communicate, attention to detail, superior service delivery and distinction in results.
Updates

I would like the brochure to be roughly about 20 pages.

Containing the following,

1) An introduction
2) Contents Page
2) What we do
3) Our Services
4) Agency & Brokerage
5) Real Estate Consulting
6) Market Research
7) Appraisal & Valuation
8) Project Management
9) Property Development

I would also like icons to represent items 4,5,6,7,8 & 9, they should be represented vertically on each of the pages from the contents page and highlighted individually on the pages that they represent.. i.e. on appraisal & valuation page, all six icons will be arranged vertically and the appraisal and valuations icon will be highlighted.

I will also like to have images that depict the services on the various pages.

I have some pages I think will flow which I will upload shortly.

Industry/Entity Type

Real Estate

Font styles to use
Serif

Colors
f78f20
0455a3

```html
<!DOCTYPE html>
<html lang="en">
<head>
<meta charset="utf-8">
<title>Halverd Property Services – Brochure</title>
<link href="https://fonts.googleapis.com/css2?family=Tinos:wght@400;700&display=swap" rel="stylesheet">
<style>
  :root {
    --bg: #dcdcdc;
    --paper: #ffffff;
    --purple: #4a3f7f;
    --purple-deep: #3f356f;
    --orange: #e3782b;
    --ink: #2f2f3a;
    --ink-soft: #55556a;
    --photo-lobby-a: #cfc6b8;
    --photo-lobby-b: #8d8476;
    --photo-site-a: #9fc3e0;
    --photo-site-b: #c9b36a;
    --photo-reader-a: #d9d6d2;
    --photo-reader-b: #4b4a55;
    --photo-plan-a: #e8e8e6;
    --photo-plan-b: #a9a9a4;
  }
  * { box-sizing: border-box; margin: 0; padding: 0; }
  html, body { width: 1200px; height: 800px; overflow: hidden; }
  body {
    background: var(--bg);
    font-family: "Tinos", "Times New Roman", serif;
    color: var(--ink);
    position: relative;
  }
  .page {
    position: absolute;
    top: 100px;
    height: 600px;
    background: var(--paper);
    box-shadow: 0 6px 18px rgba(0,0,0,0.18);
    overflow: hidden;
  }

  /* Cover */
  .cover { left: 40px; width: 360px; }
  .cover__band-top { position: absolute; left: 0; top: 0; width: 100%; height: 28px; background: var(--purple); }
  .cover__brand {
    position: absolute; right: 24px; top: 42px;
    display: flex; align-items: center; gap: 8px;
  }
  .cover__brand-mark { width: 14px; height: 14px; background: var(--orange); }
  .cover__brand-name { font-size: 22px; color: var(--purple); line-height: 1; }
  .cover__brand-sub { position: absolute; right: 24px; top: 68px; font-size: 9px; color: var(--purple); }
  .cover__rule { position: absolute; left: 0; top: 90px; width: 100%; height: 6px; background: var(--orange); }
  .cover__photo {
    position: absolute; left: 0; top: 96px; width: 100%; height: 370px;
    background: linear-gradient(160deg, var(--photo-lobby-a), var(--photo-lobby-b));
  }
  .cover__band-bottom { position: absolute; left: 0; bottom: 0; width: 100%; height: 110px; background: var(--purple); }

  /* Spread */
  .spread-left { left: 430px; width: 360px; }
  .spread-right { left: 790px; width: 360px; border-left: 1px solid #e4e4e4; }

  .services__photo {
    position: absolute; left: 0; top: 0; width: 120px; height: 190px;
    background: linear-gradient(170deg, var(--photo-plan-a), var(--photo-plan-b));
  }
  .services__title {
    position: absolute; left: 140px; top: 148px;
    font-size: 24px; font-weight: 700; color: var(--purple); letter-spacing: 0.5px;
  }
  .services__rule { position: absolute; left: 120px; top: 180px; width: 240px; height: 3px; background: var(--orange); }

  .service-box {
    position: absolute; top: 200px; height: 250px; padding: 10px 8px;
    color: #fff; font-size: 8.5px; line-height: 1.25;
  }
  .service-box h3 { font-size: 10px; font-weight: 400; margin-bottom: 3px; }
  .service-box--consulting { left: 30px; width: 112px; background: var(--orange); }
  .service-box--research { left: 148px; width: 128px; background: var(--purple); }

  .services__reader {
    position: absolute; left: 20px; top: 450px; width: 270px; height: 126px;
    background: linear-gradient(180deg, var(--photo-reader-a), var(--photo-reader-b));
  }
  .page__rule-bottom { position: absolute; left: 0; bottom: 22px; width: 100%; height: 3px; background: var(--purple); }

  .about__photo {
    position: absolute; right: 0; top: 0; width: 220px; height: 168px;
    background: linear-gradient(150deg, var(--photo-site-a), var(--photo-site-b));
  }
  .about__rule { position: absolute; left: 130px; top: 168px; width: 230px; height: 3px; background: var(--orange); }

  .column { position: absolute; top: 180px; font-size: 8px; line-height: 1.22; color: var(--ink-soft); }
  .column h2 { font-size: 10.5px; font-weight: 700; color: var(--purple); line-height: 1.1; margin-bottom: 3px; }
  .column h2.accent { color: var(--orange); }
  .column p { margin-bottom: 6px; }
  .column--services { left: 16px; width: 124px; }
  .column--about { left: 150px; width: 196px; }
</style>
</head>
<body>

  <section class="page cover">
    <div class="cover__band-top"></div>
    <div class="cover__brand">
      <span class="cover__brand-mark"></span>
      <span class="cover__brand-name">Halverd</span>
    </div>
    <div class="cover__brand-sub">Property Services</div>
    <div class="cover__rule"></div>
    <div class="cover__photo" role="img" aria-label="Bright modern office lobby with marble floor and skylight"></div>
    <div class="cover__band-bottom"></div>
  </section>

  <section class="page spread-left">
    <div class="services__photo" role="img" aria-label="Professional holding a rolled building plan"></div>
    <h1 class="services__title">SERVICES</h1>
    <div class="services__rule"></div>

    <div class="service-box service-box--consulting">
      <h3>Consulting</h3>
      <p>We provide a broad range of consulting services, we understand that our client needs may vary and our experienced team are at hand to provide tailored solutions to their needs. Our professional services include corporate planning, feasibility studies, market studies, due diligence, property tax, litigation, rent review and framework for foreign direct investment.</p>
    </div>

    <div class="service-box service-box--research">
      <h3>Market Research</h3>
      <p>Our market research team, regularly conduct surveys across a wide range of areas in both the commercial and residential markets. They regularly produce market reports that can be used for a wide range of purposes. This information also provides our team members with superior knowledge of market trends, price shifts, occupancy rates and other unique trends. The information provided allows us to provide information useful for forecasting growth and trends in the market.</p>
    </div>

    <div class="services__reader" role="img" aria-label="Smiling businessman in a suit reading a newspaper on a sofa"></div>
    <div class="page__rule-bottom"></div>
  </section>

  <section class="page spread-right">
    <div class="about__photo" role="img" aria-label="Engineers in hard hats reviewing plans on a construction site"></div>
    <div class="about__rule"></div>

    <div class="column column--services">
      <h2>Project Management&amp; Property Development</h2>
      <p>Our project management team, with vast experience across commercial and residential developments provide the much needed support to achieve your dream property or office, allowing our clients to concentrate on their core business. We provide accurate information from financing, to design concept to budgeting and construction management. We take pride in creating inspirational developments that people can live, work and enjoy, whilst adding value.</p>
      <h2 class="accent">Valuation &amp; Appraisal</h2>
      <p>We provide valuation and appraisal services to clients across a broad spectrum. Our valuation advice can provide information to assist with portfolio valuation, single asset valuation, financial reporting valuation. These services are provided to individuals, financial institutions and corporates. Appraisal methods will vary based on the specific needs of our clients.</p>
    </div>

    <div class="column column--about">
      <h2 class="accent">WHAT WE DO</h2>
      <p>Halverd is a leading property services company, incorporated in 1984, providing bespoke solutions in advisory, brokerage and turnkey solutions to owners, occupiers and property investors. Over the years we have expanded our services with a foundation based on core strengths, unrivalled local expertise, network and knowledge combined with strategic partnership. As well as providing property solutions we also develop commercial and residential units.</p>
      <p>Our growth has been based on maintaining relationships with our extensive client base, ranging from financial institutions, government agencies, airlines and servicing companies, manufacturing companies, multinationals and local corporations, to private developers and investors. Our clients depend on our ability to draw on years of experience in the local market, our professionals know their communities and the property market inside and out, and provide knowledgeable, creative solutions to all their real estate needs.</p>
      <p>The combination of our integrated services allows us to provide a superior end to end solution to our clients, customized to their own requirements. Market research is a core component to our business model, allowing us to make informed decisions based based on research findings. Our brokerage team also benefits from this information, allowing our associates to advise clients on how best to maximise return on their investment on the sale or buy side within a short timeline.</p>
      <p>We pay great attention to detail in consideration of our client requirements, delivering mandates with distinction.</p>
    </div>

    <div class="page__rule-bottom"></div>
  </section>

</body>
</html>
```